out of the box Business Card Design for a Manufacturer / Distributor

We are a manufarturer and distributor of products.
the company name is VORTANI (Pic attached)

the picture is NOT a must have on the business Card.

the Business Card should look really professional and/or special, so out of the box thinking is welcome.

there should be 2 Adresses on the Business Card for Main and Branch Office.
Email Adress, homepage, Name is required
NO Phone Number

Our working field:
Private Labeling
high Quality Production
direct distribution
warehousing
trademark registration
legal support

Main Office:
Kornblumenweg 14
08352 Feldbrück
Germany

Branch Office:
Daska Lane
Tarikpur
Pakistan

Names:
Lukas Feldhaus (Owner)
Imran Qureshi (Owner)

Email:
lukas@vortani-example.com
imran@vortani-example.com

homepage:
vortani-example.com

Industry/Entity Type

Manufacturer Distributer

Contact Information for Business Card

Vortani

Requirements
Must have
• Names, both office Adresses, email, homepage
Should not have
• Phone Number

```html
<!DOCTYPE html>
<html lang="en">
<head>
<meta charset="utf-8">
<title>VORTANI Business Card</title>
<link href="https://fonts.googleapis.com/css2?family=PT+Sans:wght@400;700&display=swap" rel="stylesheet">
<style>
  :root {
    --page: #ffffff;
    --ink: #000000;
    --paper: #ffffff;
    --front: #000000;
    --shadow: rgba(0, 0, 0, 0.35);
  }
  * { margin: 0; padding: 0; box-sizing: border-box; }
  html, body {
    width: 1200px; height: 900px; overflow: hidden;
    background: var(--page);
    font-family: "PT Sans", "Segoe UI", sans-serif;
    color: var(--ink);
  }
  .canvas { position: relative; width: 1200px; height: 900px; }
  .card {
    position: absolute; left: 285px; width: 630px; height: 360px;
    box-shadow: 4px 8px 12px var(--shadow);
    overflow: hidden;
  }
  .card--front { top: 63px; background: var(--front); }
  .card--back { top: 478px; background: var(--paper); }

  .front-brand { position: absolute; left: 406px; top: 196px; color: var(--paper); }
  .front-brand__dot {
    position: absolute; left: 48px; top: 0; width: 62px; height: 62px;
    border-radius: 50%; background: var(--paper);
  }
  .front-brand__name {
    position: absolute; left: 0; top: 78px;
    font-size: 38px; font-weight: 400; letter-spacing: 0.5px; white-space: nowrap;
  }

  .back-brand__dot {
    position: absolute; left: 100px; top: 40px; width: 42px; height: 42px;
    border-radius: 50%; background: var(--ink);
  }
  .back-brand__name {
    position: absolute; left: 153px; top: 50px;
    font-size: 22px; font-weight: 400; letter-spacing: 0.3px;
  }
  .tagline {
    position: absolute; left: 100px; top: 100px;
    font-size: 9.5px; font-weight: 700; letter-spacing: 0.2px;
  }
  .services {
    position: absolute; left: 41px; top: 133px;
    display: grid; grid-template-columns: 135px 150px; row-gap: 3px;
    list-style: none; font-size: 9px; font-weight: 700;
  }
  .services li { display: flex; align-items: center; gap: 3px; line-height: 11px; }
  .services li::before {
    content: ""; width: 8px; height: 8px; border-radius: 50%; background: var(--ink);
  }
  .owners__icon { position: absolute; left: 326px; top: 73px; }
  .owners__names {
    position: absolute; left: 367px; top: 64px;
    font-size: 25px; font-weight: 700; line-height: 24px; text-transform: uppercase;
  }
  .owners__role {
    position: absolute; left: 367px; top: 127px;
    font-size: 15px; font-weight: 400;
  }
  .divider {
    position: absolute; left: 49px; top: 187px; width: 533px; height: 2px; background: var(--ink);
  }
  .contact { position: absolute; font-size: 15px; line-height: 21.5px; white-space: nowrap; }
  .contact--email { left: 101px; top: 197px; }
  .contact--web { left: 371px; top: 207px; }
  .contact--main { left: 100px; top: 248px; }
  .contact--branch { left: 371px; top: 248px; }
  .icon { position: absolute; }
</style>
</head>
<body>
<main class="canvas">
  <section class="card card--front" aria-label="Card front">
    <div class="front-brand">
      <span class="front-brand__dot"></span>
      <span class="front-brand__name">VORTANI</span>
    </div>
  </section>

  <section class="card card--back" aria-label="Card back">
    <span class="back-brand__dot"></span>
    <span class="back-brand__name">VORTANI</span>
    <p class="tagline">MANUFACTURER &amp; DISTRIBUTER</p>
    <ul class="services">
      <li>PRIVATE LABELING</li>
      <li>HIGH QUALITY PRODUCTION</li>
      <li>DIRECT DISTRIBUTION</li>
      <li>WAREHOUSING</li>
      <li>TRADEMARK REGISTRATION</li>
      <li>LEGAL SUPPORT</li>
    </ul>

    <svg class="owners__icon" width="28" height="37" viewBox="0 0 28 37" aria-hidden="true">
      <circle cx="14" cy="8" r="8" fill="#000"/>
      <path d="M0 22 a4 4 0 0 1 4-4 h20 a4 4 0 0 1 4 4 v15 h-28z" fill="#000"/>
    </svg>
    <p class="owners__names">Lukas Feldhaus<br>Imran Qureshi</p>
    <p class="owners__role">OWNERS</p>

    <div class="divider"></div>

    <svg class="icon" style="left:65px;top:209px" width="22" height="15" viewBox="0 0 22 15" aria-hidden="true">
      <rect x="1" y="1" width="20" height="13" fill="none" stroke="#000" stroke-width="2"/>
      <path d="M1 1 L11 8 L21 1" fill="none" stroke="#000" stroke-width="2"/>
    </svg>
    <p class="contact contact--email">lukas@vortani-example.com<br>imran@vortani-example.com</p>

    <svg class="icon" style="left:333px;top:205px" width="24" height="24" viewBox="0 0 24 24" aria-hidden="true">
      <g fill="none" stroke="#000" stroke-width="2">
        <circle cx="12" cy="12" r="10.5"/>
        <ellipse cx="12" cy="12" rx="4.5" ry="10.5"/>
        <line x1="1.5" y1="12" x2="22.5" y2="12"/>
        <line x1="12" y1="1.5" x2="12" y2="22.5"/>
        <line x1="3.5" y1="6.5" x2="20.5" y2="6.5"/>
        <line x1="3.5" y1="17.5" x2="20.5" y2="17.5"/>
      </g>
    </svg>
    <p class="contact contact--web">www.vortani-example.com</p>

    <svg class="icon" style="left:65px;top:266px" width="21" height="25" viewBox="0 0 21 25" aria-hidden="true">
      <path d="M10.5 1.5 a8.5 8.5 0 0 1 8.5 8.5 c0 6-8.5 13.5-8.5 13.5 S2 16 2 10 a8.5 8.5 0 0 1 8.5-8.5z" fill="none" stroke="#000" stroke-width="2.4"/>
      <circle cx="10.5" cy="10" r="3.4" fill="none" stroke="#000" stroke-width="2.2"/>
    </svg>
    <p class="contact contact--main">Kornblumenweg 14<br>08352 Feldbrück<br>Germany&nbsp; (MAIN OFFICE)</p>

    <svg class="icon" style="left:335px;top:266px" width="21" height="25" viewBox="0 0 21 25" aria-hidden="true">
      <path d="M10.5 1.5 a8.5 8.5 0 0 1 8.5 8.5 c0 6-8.5 13.5-8.5 13.5 S2 16 2 10 a8.5 8.5 0 0 1 8.5-8.5z" fill="none" stroke="#000" stroke-width="2.4"/>
      <circle cx="10.5" cy="10" r="3.4" fill="none" stroke="#000" stroke-width="2.2"/>
    </svg>
    <p class="contact contact--branch">Daska Lane<br>Tarikpur<br>Pakistan&nbsp; (BRANCH OFFICE)</p>
  </section>
</main>
</body>
</html>
```